Business Card Design for Varnok Facility Services

We are looking for a Business Card Design for the Company "Varnok Facility Services."
Front side:
- Company Logo (small)
- Company Name, address, pohone, website and personal data.
- white background, for text e.g. company colors (blue or green like in the logo)
Please use following data:
Company data:
Varnok Facility Services Tulbrecht
Kirchmattweg 12
6331 Cham
www.varnok-fs.ch
Person data:
Ruben Tulbrecht
Geschäftsführer
+41 76 519 84 60
info@varnok-fs.ch
Back side:
could be colored in blue or green
please use a big logo sing and some smaller icons to say what is all beeing offered in facility services, like cleaning, maintenance cleaning
industrial cleaning, caretaking, gardening, disposal. There is no need for everyone of the icons if there are similar or an icon is standing for more of them.
Cleaning Service
colors to use:
blue: HEX 246BB0
green: HEX 52B33E

```html
<!DOCTYPE html>
<html lang="de">
<head>
<meta charset="utf-8">
<title>Varnok Facility Services – Visitenkarte</title>
<link rel="stylesheet" href="https://fonts.googleapis.com/css2?family=Montserrat:wght@400;500;600;700&display=swap">
<style>
  :root {
    --brand-blue: #246bb0;
    --brand-blue-deep: #1f5fa3;
    --brand-green: #52b33e;
    --card-black: #1b1b1c;
    --map-tone: #2a2a2b;
    --paper: #ffffff;
    --stage: #e9e9ea;
    --text-light: #ffffff;
  }
  * { box-sizing: border-box; margin: 0; padding: 0; }
  html, body {
    width: 1200px; height: 716px; overflow: hidden;
    background: var(--stage);
    font-family: "Montserrat", sans-serif;
  }
  .stage {
    width: 1200px; height: 716px;
    display: flex; align-items: center; justify-content: center; gap: 40px;
  }
  .card {
    position: relative;
    width: 540px; height: 310px;
    border-radius: 4px;
    overflow: hidden;
    box-shadow: 0 6px 18px rgba(0,0,0,.18);
  }

  /* Back side */
  .card--back { background: var(--card-black); }
  .back__map {
    position: absolute; inset: 24px 30px;
    border-radius: 40% 50% 45% 40%;
    background: radial-gradient(ellipse at 50% 45%, var(--map-tone) 0%, rgba(42,42,43,.6) 55%, rgba(27,27,28,0) 75%);
  }
  .back__brand {
    position: absolute; left: 0; right: 0; top: 50%;
    transform: translateY(-50%);
    display: flex; align-items: center; justify-content: center; gap: 14px;
  }
  .brand-dot {
    width: 18px; height: 18px; border-radius: 50%;
    background: var(--brand-green);
    flex: none;
  }
  .brand-name {
    font-weight: 600;
    color: var(--brand-blue);
    letter-spacing: .04em;
    line-height: 1.15;
  }
  .back__brand .brand-name { font-size: 30px; }

  /* Front side */
  .card--front { background: var(--paper); }
  .front__shape { position: absolute; inset: 0; }
  .front__details {
    position: absolute; left: 30px; top: 74px;
    color: var(--text-light);
  }
  .person__name { font-size: 19px; font-weight: 700; }
  .person__role { font-size: 13px; font-weight: 400; margin-top: 2px; }
  .address { font-size: 13px; line-height: 1.45; margin-top: 8px; font-style: normal; }
  .contact { list-style: none; margin-top: 6px; font-size: 13px; line-height: 1.5; }
  .contact li { display: flex; align-items: center; gap: 7px; }
  .contact svg { width: 10px; height: 10px; flex: none; }
  .contact .web { font-weight: 600; }
  .front__brand {
    position: absolute; left: 330px; top: 110px; width: 190px;
    display: flex; align-items: center; gap: 10px;
  }
  .front__brand .brand-name { font-size: 22px; }
</style>
</head>
<body>
<main class="stage">

  <section class="card card--back" aria-label="Rückseite">
    <div class="back__map" role="img" aria-label="Dezente Weltkarte im Hintergrund"></div>
    <div class="back__brand">
      <span class="brand-dot"></span>
      <span class="brand-name">Varnok Facility Services</span>
    </div>
  </section>

  <section class="card card--front" aria-label="Vorderseite">
    <svg class="front__shape" viewBox="0 0 540 310" preserveAspectRatio="none" aria-hidden="true">
      <path d="M0 0 H292 C205 85 210 230 420 310 H0 Z" fill="var(--brand-blue)"/>
      <path d="M300 0 C212 85 216 230 430 310" fill="none" stroke="var(--brand-green)" stroke-width="4"/>
    </svg>

    <div class="front__details">
      <p class="person__name">Ruben Tulbrecht</p>
      <p class="person__role">Geschäftsführer</p>
      <address class="address">Kirchmattweg 12<br>6331 Cham</address>
      <ul class="contact">
        <li>
          <svg viewBox="0 0 10 10" aria-hidden="true"><path d="M2 1 L4 3 L3 4 Q4.5 6 6 7 L7 6 L9 8 L7.5 9.5 Q3 8.5 .5 2.5 Z" fill="#fff"/></svg>
          +41 76 519 84 60
        </li>
        <li>
          <svg viewBox="0 0 10 10" aria-hidden="true"><rect x=".8" y="2" width="8.4" height="6" fill="none" stroke="#fff" stroke-width="1"/><path d="M1 2.3 L5 5.5 L9 2.3" fill="none" stroke="#fff" stroke-width="1"/></svg>
          info@varnok-fs.ch
        </li>
        <li class="web">
          <svg viewBox="0 0 10 10" aria-hidden="true"><circle cx="5" cy="5" r="4.2" fill="none" stroke="#fff" stroke-width="1"/><ellipse cx="5" cy="5" rx="1.8" ry="4.2" fill="none" stroke="#fff" stroke-width=".8"/><path d="M1 5 H9" stroke="#fff" stroke-width=".8"/></svg>
          www.varnok-fs.ch
        </li>
      </ul>
    </div>

    <div class="front__brand">
      <span class="brand-dot"></span>
      <span class="brand-name">Varnok Facility Services</span>
    </div>
  </section>

</main>
</body>
</html>
```